Corvantis websites redesign

Www.cor-vantis.com needs to be redesigned along with updations. The incremental material will be provided for the updations. We are looking for complete redesign of the pages with the new content. The complete write up will be provided soon

Target Market(s)

Global

Coding

Coded - Design and coding required

Number of Pages Required

5+ page

Requirements
Must have
• A clean and slick design for the Consulting.
Should not have
• Too many pictures which reduces the speed of the site

```html
<!DOCTYPE html>
<html lang="en">
<head>
<meta charset="utf-8">
<title>Corvantis – Case Studies</title>
<link href="https://fonts.googleapis.com/css2?family=Raleway:wght@300;400;500&family=Arimo:wght@400;700&display=swap" rel="stylesheet">
<style>
:root{
  --accent:#2f9fc6;
  --ink:#333;
  --muted:#555;
  --band:#f1f1f1;
  --rule:#d8d8d8;
  --footer:#1b1b1b;
  --footer-text:#a9a9a9;
  --footer-head:#ececec;
  --brand:#2b2d4a;
}
*{margin:0;padding:0;box-sizing:border-box}
html,body{width:1089px;height:1200px;overflow:hidden;background:#fff}
body{position:relative;font-family:"Arimo",Arial,sans-serif;color:var(--ink)}
.abs{position:absolute}
/* header */
.site-header{position:absolute;left:0;top:0;width:1089px;height:58px;background:#fff;box-shadow:0 1px 2px rgba(0,0,0,.06)}
.brand{position:absolute;left:245px;top:14px;display:flex;align-items:center;gap:7px;font-family:"Raleway",sans-serif;font-weight:500;font-size:20px;color:var(--brand)}
.brand-dot{width:22px;height:22px;border-radius:50%;background:var(--brand)}
.main-nav a{position:absolute;top:27px;font-size:10px;color:#666;text-decoration:none;white-space:nowrap}
.main-nav a.active{color:var(--accent)}
.nav-underline{position:absolute;left:730px;top:56px;width:48px;height:2px;background:var(--accent)}
/* reach band */
.reach{position:absolute;left:0;top:58px;width:1089px;height:326px;background:var(--band)}
.reach h1{position:absolute;left:0;width:1089px;top:52px;text-align:center;font-family:"Raleway",sans-serif;font-weight:300;font-size:21px;color:#555;letter-spacing:.2px}
.world-map{position:absolute;left:360px;top:106px;width:390px;height:188px;background:var(--accent);border-radius:40px 60px 30px 50px;opacity:.9}
.pin{position:absolute;width:5px;height:5px;border-radius:50%;background:#111}
.lead{position:absolute;height:1px;background:#111}
.pin-label{position:absolute;font-size:7.5px;color:#444;white-space:nowrap}
/* case studies */
.section-title{position:absolute;left:245px;top:427px;font-family:"Raleway",sans-serif;font-weight:300;font-size:19px;color:#444}
.section-intro{position:absolute;left:245px;top:458px;font-size:7.5px;color:var(--muted)}
.case-card{position:absolute;width:286px;height:194px;border:1px solid var(--rule);background:#fff}
.case-icon{position:absolute;left:38px;top:23px;width:34px;height:34px}
.case-title{position:absolute;left:38px;top:72px;width:220px;font-size:9.5px;line-height:13px;color:#444}
.case-rule{position:absolute;left:38px;top:110px;width:219px;height:1px;background:var(--rule)}
.case-links{position:absolute;left:38px;top:126px;list-style:none}
.case-links li{font-size:8px;color:#555;height:17px}
/* footer */
.site-footer{position:absolute;left:0;top:958px;width:1089px;height:242px;background:var(--footer);color:var(--footer-text)}
.footer-brand{position:absolute;left:245px;top:44px;display:flex;align-items:center;gap:6px;font-family:"Raleway",sans-serif;font-size:15px;color:#bbb}
.footer-brand .brand-dot{width:17px;height:17px;background:#bbb}
.address{position:absolute;left:247px;top:80px;font-size:7.6px;line-height:13px}
.contact-line{position:absolute;left:247px;font-size:7.6px}
.contact-line b{color:var(--accent);font-size:8.5px}
.contact-line a{color:var(--accent)}
.footer-head{position:absolute;font-family:"Raleway",sans-serif;font-weight:500;font-size:9px;color:var(--footer-head);letter-spacing:.3px}
.footer-head::after{content:"";position:absolute;left:0;top:14px;width:19px;height:1px;background:#777}
.mail-note{position:absolute;left:438px;top:81px;font-size:7.6px}
.mail-field{position:absolute;left:438px;top:100px;width:137px;height:24px;border:1px solid #666;font-size:7.6px;color:#ccc;padding:7px 0 0 9px}
.mail-field svg{position:absolute;right:6px;top:7px}
.site-links{position:absolute;left:631px;top:77px;list-style:none}
.site-links li{font-size:7.6px;height:16.4px;color:#bbb}
.site-links li::before{content:"»";margin-right:6px;color:#777}
.site-links li.current{color:var(--accent);text-decoration:underline}
.social{position:absolute;width:20px;height:20px;border-radius:50%;border:1px solid #bbb;top:80px}
.social.active{border-color:var(--accent)}
.footer-bottom{position:absolute;left:0;top:204px;width:1089px;height:1px;background:#2c2c2c}
.copyright{position:absolute;left:246px;top:220px;font-size:7.6px;color:#8a8a8a}
</style>
</head>
<body>

<header class="site-header">
  <div class="brand"><span class="brand-dot"></span>Corvantis</div>
  <nav class="main-nav">
    <a style="left:513px">Home</a>
    <a style="left:561px">Founder</a>
    <a style="left:612px">Consultancy</a>
    <a style="left:680px">Platform</a>
    <a class="active" style="left:729px">Case Studies</a>
    <a style="left:798px">Contact Us</a>
  </nav>
  <div class="nav-underline"></div>
</header>

<section class="reach">
  <h1>Geographical Reach – Corporate Deals Placed</h1>
  <div class="world-map" role="img" aria-label="World map marking corporate deals placed in the US, Morocco, Kuwait, Dubai, Hong Kong and Singapore"></div>

  <span class="pin-label" style="left:312px;top:159px">US 10.0</span>
  <div class="lead" style="left:344px;top:163px;width:64px"></div>
  <div class="pin" style="left:406px;top:161px"></div>

  <span class="pin-label" style="left:450px;top:168px">Morocco 8.4</span>
  <div class="lead" style="left:496px;top:173px;width:34px"></div>
  <div class="pin" style="left:528px;top:171px"></div>

  <span class="pin-label" style="left:461px;top:180px">Kuwait 80.0</span>
  <div class="lead" style="left:505px;top:183px;width:84px"></div>
  <div class="pin" style="left:587px;top:181px"></div>

  <div class="pin" style="left:592px;top:189px"></div>
  <div class="lead" style="left:596px;top:191px;width:96px"></div>
  <span class="pin-label" style="left:695px;top:186px">Dubai 27.6</span>

  <div class="pin" style="left:674px;top:178px"></div>
  <div class="lead" style="left:678px;top:180px;width:32px"></div>
  <span class="pin-label" style="left:713px;top:175px">Hong Kong 13.0</span>

  <div class="pin" style="left:660px;top:207px"></div>
  <div class="lead" style="left:664px;top:209px;width:53px"></div>
  <span class="pin-label" style="left:720px;top:205px">Singapore 6.0</span>
</section>

<h2 class="section-title">Case Studies</h2>
<p class="section-intro">Some of the deals completed by CCL are summarised below to describe the range of activities undertaken with Corporates</p>

<article class="case-card" style="left:245px;top:489px">
  <svg class="case-icon" viewBox="0 0 34 34" aria-hidden="true">
    <rect x="1" y="24" width="8" height="10" fill="var(--accent)"/>
    <rect x="12" y="19" width="8" height="15" fill="var(--accent)"/>
    <rect x="23" y="13" width="8" height="21" fill="var(--accent)"/>
    <polyline points="1,20 11,11 17,15 29,3" fill="none" stroke="var(--accent)" stroke-width="3"/>
    <polygon points="24,1 32,0 31,8" fill="var(--accent)"/>
  </svg>
  <h3 class="case-title" style="font-weight:400">Export Credit Agency backed long term Project financing</h3>
  <div class="case-rule"></div>
  <ul class="case-links"><li>Case Study 1 - Download as PDF</li></ul>
</article>

<article class="case-card" style="left:558px;top:489px">
  <svg class="case-icon" viewBox="0 0 42 34" aria-hidden="true" style="width:42px">
    <circle cx="22" cy="12" r="6" fill="var(--accent)"/>
    <circle cx="29" cy="4" r="3.5" fill="var(--accent)"/>
    <path d="M1 24 Q10 19 19 23 L28 22 Q30 23 28 25 L18 26 L30 25 L40 18 Q43 19 40 23 L30 31 Q22 34 12 31 L1 30 Z" fill="var(--accent)"/>
  </svg>
  <h3 class="case-title" style="font-weight:400">Introducing Regional/Local banks for International Subsidiary Banking</h3>
  <div class="case-rule"></div>
  <ul class="case-links">
    <li>Case Study 1 - Download as PDF</li>
    <li>Case Study 2- Download as PDF</li>
    <li>Case Study 3 - Download as PDF</li>
  </ul>
</article>

<article class="case-card" style="left:245px;top:707px">
  <svg class="case-icon" viewBox="0 0 34 34" aria-hidden="true">
    <circle cx="18" cy="17" r="14" fill="var(--accent)"/>
    <path d="M4 17 H32 M18 3 V31 M8 8 Q18 13 28 8 M8 26 Q18 21 28 26" stroke="#fff" stroke-width="1.5" fill="none"/>
    <rect x="1" y="4" width="9" height="26" fill="var(--accent)"/>
    <path d="M9 8 Q3 8 3 12 Q3 16 6 16 Q9 17 9 21 Q9 25 3 25" stroke="#fff" stroke-width="2" fill="none"/>
  </svg>
  <h3 class="case-title" style="top:79px;font-weight:400">Structured Financing</h3>
  <div class="case-rule"></div>
  <ul class="case-links"><li>Case Study 1 - Download as PDF</li></ul>
</article>

<article class="case-card" style="left:558px;top:707px">
  <svg class="case-icon" viewBox="0 0 34 34" aria-hidden="true">
    <path d="M16 3 A15 15 0 1 0 31 18 L16 18 Z" fill="var(--accent)"/>
    <path d="M19 0 A15 15 0 0 1 34 15 L19 15 Z" fill="var(--accent)"/>
  </svg>
  <h3 class="case-title" style="top:79px;font-weight:400">Bank Lines Business</h3>
  <div class="case-rule"></div>
  <ul class="case-links">
    <li>Case Study 1 - Download as PDF</li>
    <li>Case Study 2- Download as PDF</li>
  </ul>
</article>

<footer class="site-footer">
  <div class="footer-brand"><span class="brand-dot"></span>Corvantis</div>
  <p class="address">Corvantis Consultancy Ltd<br>Suite 08, 21st Floor, Meridian Harbour<br>Tower, 47 Lantern Quay Road, Kowloon<br>Hong Kong</p>
  <p class="contact-line" style="top:146px">T: <b>852-390 16257</b></p>
  <p class="contact-line" style="top:160px">E: <a>query@cor-vantis.com</a></p>

  <h4 class="footer-head" style="left:438px;top:52px">GET IN TOUCH!</h4>
  <p class="mail-note">Simply Drop Your Mail Here</p>
  <div class="mail-field">Your Email Here
    <svg width="11" height="8" viewBox="0 0 11 8" aria-hidden="true"><rect x=".5" y=".5" width="10" height="7" fill="none" stroke="var(--accent)"/><polyline points=".5,.5 5.5,4.5 10.5,.5" fill="none" stroke="var(--accent)"/></svg>
  </div>

  <h4 class="footer-head" style="left:631px;top:52px">SITE LINKS</h4>
  <ul class="site-links">
    <li>Home</li><li>Founder</li><li>Consultancy</li><li>Platform</li><li class="current">Case Studies</li><li>Contact Us</li>
  </ul>

  <h4 class="footer-head" style="left:757px;top:52px">SOCIAL LINKS</h4>
  <span class="social active" style="left:758px" aria-label="Social profile"></span>
  <span class="social" style="left:780px" aria-label="Social profile"></span>
  <span class="social" style="left:802px" aria-label="Social profile"></span>
  <span class="social" style="left:824px" aria-label="Social profile"></span>

  <div class="footer-bottom"></div>
  <p class="copyright">© 2016. Corvantis Consultancy Limited</p>
</footer>

</body>
</html>
```